Pretzel Company needs a Pretzel Bag Design for Retail

Benny Twists, a smoked, seasoned pretzel maker, needs an eye popping pretzel package design that will make consumers excited to try their smoked, seasoned pretzels

```html
<!DOCTYPE html>
<html lang="en">
<head>
<meta charset="utf-8">
<title>Benny Twists – Pretzel Bag</title>
<link rel="stylesheet" href="https://fonts.googleapis.com/css2?family=Arimo:wght@400;700&family=Bebas+Neue&family=League+Gothic&display=swap">
<style>
  :root {
    --slate: #2e4a66;
    --bag-blue: #1d4282;
    --tan: #ebc9a0;
    --pretzel-light: #f2b566;
    --pretzel: #d98a33;
    --pretzel-dark: #9c5a1c;
    --red: #d8282a;
    --white: #ffffff;
    --ink: #111111;
    --paper: #ffffff;
  }
  * { box-sizing: border-box; margin: 0; padding: 0; }
  html, body { width: 1200px; height: 400px; overflow: hidden; background: var(--paper); }
  .canvas { position: relative; width: 1200px; height: 400px; font-family: "Arimo", Arial, sans-serif; }

  /* Brand panel */
  .brand-panel {
    position: absolute; left: 0; top: 0; width: 250px; height: 400px;
    background: var(--slate);
    display: flex; flex-direction: column; justify-content: space-around; align-items: center;
    padding: 30px 0;
  }
  .brand-lockup { display: flex; align-items: center; gap: 10px; }
  .brand-lockup .dot { width: 22px; height: 22px; border-radius: 50%; background: var(--tan); flex: none; }
  .brand-lockup .dot.grey { background: #c9ccd1; }
  .brand-name {
    font-family: "Bebas Neue", sans-serif; font-size: 40px; line-height: 1;
    color: var(--white); letter-spacing: 1px; white-space: nowrap;
  }

  /* Bags */
  .bag {
    position: absolute; top: 18px; width: 205px; height: 337px;
    background: var(--bag-blue); overflow: hidden; color: var(--white);
  }
  .bag-front { left: 463px; }
  .bag-back { left: 783px; }
  .view-label {
    position: absolute; top: 362px; width: 205px; text-align: center;
    font-size: 26px; color: var(--ink); letter-spacing: 1px;
  }
  .view-label.front { left: 463px; }
  .view-label.back { left: 783px; }

  /* Pretzel illustration areas: soft golden-baked gradient */
  .pretzel-art {
    position: absolute; border-radius: 46% 54% 50% 50% / 52% 48% 52% 48%;
    background:
      radial-gradient(circle at 32% 28%, rgba(255,236,200,0.55) 0%, rgba(255,236,200,0) 38%),
      radial-gradient(circle at 50% 50%, var(--pretzel-light) 0%, var(--pretzel) 55%, var(--pretzel-dark) 100%);
    box-shadow: 2px 3px 6px rgba(0,0,0,0.35);
  }

  /* Front */
  .banner {
    position: absolute; left: 51px; top: 0; width: 103px; height: 147px;
    background: var(--tan);
    clip-path: polygon(0 0, 100% 0, 100% 88%, 50% 100%, 0 88%);
    display: flex; align-items: center; justify-content: center;
  }
  .banner .brand-lockup { flex-direction: column; gap: 6px; margin-top: 4px; }
  .banner .brand-name { color: var(--bag-blue); font-size: 26px; text-align: center; white-space: normal; line-height: 0.95; }
  .banner .dot { width: 18px; height: 18px; background: var(--pretzel); }

  .claim {
    position: absolute; left: 0; top: 160px; width: 205px;
    font-family: "Bebas Neue", sans-serif; font-size: 18px; letter-spacing: 1.4px; line-height: 1;
    display: flex; justify-content: center; align-items: center; gap: 4px;
  }
  .claim .mini-pretzel { width: 7px; height: 7px; border-radius: 50%; background: var(--pretzel); flex: none; }
  .product-name {
    position: absolute; left: 0; top: 176px; width: 205px; text-align: center;
    font-family: "League Gothic", sans-serif; font-weight: 400; font-size: 74px; line-height: 1;
    transform: scaleX(0.78); transform-origin: center;
  }
  .tagline {
    position: absolute; left: 0; top: 256px; width: 205px; text-align: center;
    font-family: "Bebas Neue", sans-serif; font-size: 8.4px; letter-spacing: 0.3px; line-height: 1;
  }
  .flavor {
    position: absolute; left: 70px; top: 266px; width: 62px; height: 11px;
    background: var(--red); text-align: center;
    font-family: "Bebas Neue", sans-serif; font-size: 11px; line-height: 11.5px; letter-spacing: 0.6px;
  }
  .net-weight {
    position: absolute; left: 0; top: 281px; width: 205px; text-align: center;
    font-family: "League Gothic", sans-serif; font-size: 10px; line-height: 1;
  }
  .website {
    position: absolute; left: 66px; top: 310px;
    font-family: "Arimo", sans-serif; font-size: 6px; letter-spacing: 0.2px;
  }
  .partner-badge {
    position: absolute; left: 164px; top: 306px; width: 24px; height: 15px;
    border-radius: 50%; background: var(--white); border: 1.5px solid #e4b53a;
  }

  /* Back */
  .back-logo { position: absolute; left: 0; top: 58px; width: 205px; display: flex; justify-content: center; }
  .back-logo .brand-name { font-size: 24px; }
  .back-logo .dot { width: 14px; height: 14px; }
  .story { position: absolute; left: 24px; top: 100px; width: 88px; font-size: 3.6px; line-height: 1.3; }
  .story h3 { font-size: 4.4px; font-weight: 400; margin-bottom: 4px; }
  .story p { margin-bottom: 3px; }
  .story .history-title { font-size: 4.2px; margin: 0 0 3px; }
  .story .history { position: absolute; top: 82px; left: 0; width: 88px; }
  .story-icon { left: 51px; top: 151px; width: 21px; height: 20px; box-shadow: none; }

  .nutrition {
    position: absolute; left: 127px; top: 99px; width: 55px; height: 132px;
    background: var(--white); color: var(--ink); padding: 3px;
    font-size: 2.9px; line-height: 1.3; overflow: hidden;
  }
  .nutrition .title { font-weight: 700; font-size: 6px; border-bottom: 0.6px solid var(--ink); line-height: 1.1; }
  .nutrition .serving { border-bottom: 2px solid var(--ink); padding-bottom: 1px; }
  .nutrition .calories { display: flex; justify-content: space-between; font-weight: 700; font-size: 4.6px; border-bottom: 1.2px solid var(--ink); }
  .nutrition .row { display: flex; justify-content: space-between; border-bottom: 0.3px solid var(--ink); }
  .nutrition .row.indent { padding-left: 3px; }
  .nutrition .row.thick { border-bottom: 1.4px solid var(--ink); }
  .nutrition .ingredients { margin-top: 3px; }

  .divider { position: absolute; left: 58px; top: 246px; width: 96px; height: 1.4px; background: var(--red); }
  .pitch {
    position: absolute; left: 24px; top: 254px; width: 157px; text-align: center;
    font-size: 4.3px; line-height: 1.3;
  }
  .follow {
    position: absolute; left: 0; top: 301px; width: 205px; text-align: center;
    font-size: 3.6px; letter-spacing: 0.2px;
  }
</style>
</head>
<body>
<main class="canvas">

  <section class="brand-panel" aria-label="Brand mark versions">
    <div class="brand-lockup"><span class="dot"></span><span class="brand-name">Benny Twists</span></div>
    <div class="brand-lockup"><span class="dot grey"></span><span class="brand-name">Benny Twists</span></div>
    <div class="brand-lockup"><span class="brand-name">Benny Twists</span></div>
  </section>

  <article class="bag bag-front" aria-label="Bag front">
    <div class="pretzel-art" style="left:176px; top:-14px; width:44px; height:40px;" role="img" aria-label="Golden salted pretzel illustration cropped at the top right corner"></div>
    <div class="pretzel-art" style="left:-22px; top:50px; width:44px; height:86px;" role="img" aria-label="Golden salted pretzel illustration peeking in from the left edge"></div>
    <div class="pretzel-art" style="left:182px; top:126px; width:44px; height:76px;" role="img" aria-label="Golden salted pretzel illustration peeking in from the right edge"></div>
    <div class="pretzel-art" style="left:-18px; top:268px; width:84px; height:86px;" role="img" aria-label="Large golden salted pretzel illustration in the bottom left corner"></div>

    <div class="banner">
      <div class="brand-lockup"><span class="dot"></span><span class="brand-name">Benny<br>Twists</span></div>
    </div>

    <div class="claim"><span class="mini-pretzel" role="img" aria-label="Small pretzel icon"></span>Seasoned, Smoked<span class="mini-pretzel" role="img" aria-label="Small pretzel icon"></span></div>
    <h1 class="product-name">PRETZELS</h1>
    <p class="tagline">Perfect crunch that almost melts in your mouth</p>
    <p class="flavor">-Original-</p>
    <p class="net-weight">NET WT 12oz (340g)</p>
    <p class="website">www.bennytwistsnacks.com</p>
    <div class="partner-badge" role="img" aria-label="Regional producer badge"></div>
  </article>
  <p class="view-label front">FRONT</p>

  <article class="bag bag-back" aria-label="Bag back">
    <div class="back-logo">
      <div class="brand-lockup"><span class="dot"></span><span class="brand-name">Benny Twists</span></div>
    </div>

    <div class="story">
      <h3>Benny Twists - Prairie Hearth Foods LLC</h3>
      <p>My pretzels are Seasoned and slow smoked to perfection. Born in a bar and named after my dad!</p>
      <p>The most common reaction from people is the texture of them, not too crunchy not too soft, the perfect crunch that almost melts in your mouth. The flavor is described as unique with the perfect amount of smoke.</p>
      <div class="history">
        <p class="history-title">History:</p>
        <p>Created in 2020 in a bar as a snack to serve to our customers while they drank beer. When we decided to close the doors because of the distance we lived from the bar. After we closed, our customers would contact me for my pretzels because they couldn't stop craving them. That is when I got the idea to start making them on a bigger scale and selling them. Long story short they have really become a hit and currently in the process of mass production.</p>
      </div>
    </div>
    <div class="pretzel-art story-icon" role="img" aria-label="Small pretzel illustration"></div>

    <div class="nutrition" aria-label="Nutrition facts">
      <p class="title">Nutrition Facts</p>
      <p>12 servings per container</p>
      <p class="serving"><b>Serving size 15 pretzels (28g)</b></p>
      <p>Amount per serving</p>
      <p class="calories"><span>Calories</span><span>130</span></p>
      <p class="row" style="justify-content:flex-end">% Daily Value</p>
      <p class="row"><span><b>Total Fat</b> 7g</span><span>9%</span></p>
      <p class="row indent"><span>Saturated Fat 1g</span><span>4%</span></p>
      <p class="row"><span><b>Cholesterol</b> 0mg</span><span>0%</span></p>
      <p class="row"><span><b>Sodium</b> 350mg</span><span>15%</span></p>
      <p class="row"><span><b>Total Carbohydrate</b> 17g</span><span>6%</span></p>
      <p class="row thick"><span><b>Protein</b> 2g</span><span></span></p>
      <p class="row"><span>Iron 1mg</span><span>6%</span></p>
      <p class="ingredients">INGREDIENTS: Pretzels (wheat flour, salt, vegetable oil, malt syrup, yeast, baking soda), seasoning blend, buttermilk, garlic, onion, paprika, chili pepper, natural smoke flavor, sea salt. <b>CONTAINS: WHEAT, SOY, MILK.</b></p>
    </div>

    <div class="divider"></div>
    <p class="pitch">Take your snack game to the next level with Benny's Twists! Each golden-brown twist is infused with a rich smoky flavor and finished off with a dash of sea salt, creating a mouthwatering combination of savory goodness. Crunchy, bold, and absolutely irresistible!</p>
    <p class="follow">FOLLOW US</p>
  </article>
  <p class="view-label back">BACK</p>

</main>
</body>
</html>
```